Schema Paladin Powerpoint with Commander Ravelle Type Theme

Need powerpoint template with matching colors and different slide options. Logo and colors to be used can be found at schemapaladinhq.com. Want brightly colored slide deck that is readable form the back of a room, but highlights colors. I will be incorporating Trivano into the slides to gamify my presentations.

Target Market(s)

Tech

Industry/Entity Type

IT, specifically database, but crossing over to mental health in IT, important note this is not for a company, this is just for a professional building a brand

Font styles to use
Sans Serif

Colors
0054AA
0677BA
7BADD7
CADEEF
E8F1F8
EB3D1F
EC4F4E
F09395
F8D3D4
FCEDEE

Requirements
Must have
• My Logo in the bottom corner, front page, a thank your page, question page, content page, content page with two columns, content page with graphs, and icons to be used in the primary colors of the logos, About Me Page, Break Slides, Demo break slide
Should not have
• Lighter shades of colors, I want to pop out where colors are used, I want spacing and font size to be readable from the back of a room, most likely black text and white background

```html
<!DOCTYPE html>
<html lang="en">
<head>
<meta charset="utf-8">
<title>Schema Paladin — Presentation Theme Overview</title>
<link href="https://fonts.googleapis.com/css2?family=Poppins:wght@300;400;500;600;700&display=swap" rel="stylesheet">
<style>
:root{
  --navy:#1e4280;
  --navy-deep:#173567;
  --red:#e8272c;
  --dark:#3d3d3d;
  --gray:#8c8c8c;
  --light:#eef1f5;
  --ink:#3a3a3a;
  --page:#e4e5e8;
  --white:#ffffff;
}
*{box-sizing:border-box;margin:0;padding:0}
html,body{width:1200px;height:3630px;overflow:hidden;background:var(--page)}
body{font-family:"Poppins",sans-serif;color:var(--ink)}
.deck{display:grid;grid-template-columns:repeat(3,386px);grid-template-rows:repeat(16,217px);gap:9px;padding:11px}
.slide{position:relative;overflow:hidden;background:var(--white)}
.bg-navy{background:var(--navy)}
.bg-dark{background:var(--dark)}
.bg-red{background:var(--red)}
.photo{position:absolute;background:linear-gradient(135deg,#2c4f8a 0%,#1c3a6e 55%,#13294f 100%)}
.photo-navy{position:absolute;inset:0;background:linear-gradient(120deg,rgba(30,66,128,.95),rgba(24,52,104,.86)),linear-gradient(45deg,#3c5f96,#14294f)}
.photo-light{position:absolute;background:linear-gradient(135deg,#c9d2de,#8b9bb2 60%,#5b6b84)}
.abs{position:absolute}
.brand{position:absolute;font-weight:700;color:var(--navy);display:flex;align-items:center;gap:4px;white-space:nowrap;letter-spacing:.2px}
.brand .dot{width:1em;height:1em;border-radius:50%;background:currentColor;display:inline-block}
.brand.white{color:var(--white)}
.corner{position:absolute;top:4px;right:5px;font-size:4px;font-weight:700;color:var(--navy)}
.side{position:absolute;right:3px;top:64px;writing-mode:vertical-rl;font-size:5px;font-weight:700;color:var(--red);letter-spacing:.3px}
.side.left{right:auto;left:3px}
.side.white{color:var(--white)}
.pg{position:absolute;bottom:4px;right:18px;font-size:4px;color:var(--gray)}
.pg.left{right:auto;left:10px}
.dash{position:absolute;width:16px;height:3px;background:var(--red)}
.h-title{position:absolute;left:0;right:0;top:16px;text-align:center;font-size:14px;font-weight:600;color:var(--navy)}
.h-title::after{content:"";display:block;width:14px;height:3px;background:var(--red);margin:4px auto 0}
.h-left{position:absolute;font-size:14px;font-weight:600;color:var(--navy)}
.h-left::after{content:"";display:block;width:14px;height:3px;background:var(--red);margin-top:3px}
.h-left.white{color:var(--white)}
.fine{font-size:4.4px;line-height:1.45;color:#555}
.fine.white{color:#dfe6f2}
.label{font-size:5px;font-weight:600;color:var(--ink)}
.pill{position:absolute;background:var(--red);color:var(--white);border-radius:8px;font-weight:600;text-align:center}
.card{position:absolute;color:var(--white);text-align:center;padding:24px 5px 4px}
.card .ic{position:absolute;top:6px;left:50%;transform:translateX(-50%);width:16px;height:16px;border-radius:50%;border:1.2px solid #fff;background:rgba(255,255,255,.15)}
.card .nm{font-size:5px;font-weight:600;margin-bottom:3px}
.card .tx{font-size:3.8px;line-height:1.45;opacity:.9}
.c-red{background:var(--red)}.c-navy{background:var(--navy)}.c-deep{background:#1b3560}.c-gray{background:#8a8a8a}
table{border-collapse:collapse;width:100%}
.tbl td,.tbl th{font-size:3.8px;padding:0 3px;height:10px;text-align:left;color:#666}
.tbl th{color:#fff;font-weight:600}
</style>
</head>
<body>
<main class="deck">

<!-- 1 cover photo -->
<section class="slide">
  <div class="photo-navy" role="img" aria-label="Photo of hands typing on a laptop, navy tinted"></div>
  <div class="brand white" style="left:150px;top:40px;font-size:8px"><span class="dot"></span>Schema Paladin</div>
  <div class="abs" style="left:0;right:0;top:78px;text-align:center;color:#dfe6f2;font-size:5px;letter-spacing:.5px">www.schemapaladinhq.com</div>
  <div class="abs" style="left:0;right:0;top:92px;text-align:center;color:#fff;font-size:23px;font-weight:600;line-height:1">Presentation<br>Title Goes Here</div>
  <div class="abs" style="left:0;right:0;top:147px;text-align:center;color:#dfe6f2;font-size:7px">Sub Title Goes Here</div>
  <div class="pill" style="left:160px;top:188px;width:66px;height:11px;font-size:5px;line-height:11px">Oct 2021</div>
</section>

<!-- 2 cover strip -->
<section class="slide">
  <div class="photo" style="left:0;top:0;right:0;height:182px" role="img" aria-label="Photo of a desk workspace, navy tinted"></div>
  <div class="abs" style="left:20px;top:70px;color:#fff;font-size:17px;font-weight:600;line-height:1.2">TITLE OF<br>PRESENTATION</div>
  <div class="abs fine white" style="left:20px;top:140px">Here is A place for Credentials<br>Date: 2021 March</div>
  <div class="brand" style="left:12px;top:196px;font-size:7px"><span class="dot"></span>Schema Paladin</div>
  <div class="abs" style="right:28px;top:200px;font-size:5px;font-weight:600;color:var(--navy)">Presenter Name</div>
</section>

<!-- 3 cover full -->
<section class="slide">
  <div class="photo-navy" role="img" aria-label="Photo of server racks, navy tinted"></div>
  <div class="brand white" style="left:24px;top:64px;font-size:7px"><span class="dot"></span>Schema Paladin</div>
  <div class="abs" style="left:24px;top:88px;color:#fff;font-size:17px;font-weight:600;line-height:1.2">TITLE OF<br>PRESENTATION</div>
  <div class="abs fine white" style="left:24px;top:150px">Here is A place for Credentials<br>Date: 2021 March</div>
</section>

<!-- 4 cover red band -->
<section class="slide bg-navy">
  <div class="photo-light" style="left:160px;top:0;right:0;height:120px" role="img" aria-label="Photo of a laptop on a desk"></div>
  <div class="photo-light" style="left:150px;top:178px;width:80px;height:39px" role="img" aria-label="Photo of hands on a keyboard"></div>
  <div class="brand white" style="left:40px;top:56px;font-size:10px"><span class="dot"></span>Schema Paladin</div>
  <div class="abs" style="left:100px;top:118px;width:300px;height:58px;background:var(--red);transform:skewX(-22deg)"></div>
  <div class="abs" style="left:175px;top:120px;width:200px;text-align:center;color:#fff;font-size:18px;font-weight:600;line-height:1.05">Presentation<br>Title Goes Here</div>
</section>

<!-- 5 cover white -->
<section class="slide">
  <div class="brand" style="left:26px;top:50px;font-size:8px"><span class="dot"></span>Schema Paladin</div>
  <div class="abs" style="left:24px;top:80px;color:var(--navy);font-size:23px;font-weight:600;line-height:1.05">Presentation<br>Title Goes Here</div>
  <div class="abs" style="left:24px;top:132px;color:var(--red);font-size:7px">Sub Title Goes Here</div>
  <div class="pill" style="left:22px;top:170px;width:118px;height:12px;font-size:5px;line-height:12px;letter-spacing:.6px">www.schemapaladinhq.com</div>
</section>

<!-- 6 plain white -->
<section class="slide">
  <div class="brand" style="left:146px;top:20px;font-size:8px"><span class="dot"></span>Schema Paladin</div>
</section>

<!-- 7-9 colour fills -->
<section class="slide bg-navy"><div class="brand white" style="left:146px;top:20px;font-size:8px"><span class="dot"></span>Schema Paladin</div></section>
<section class="slide bg-dark"><div class="brand white" style="left:146px;top:20px;font-size:8px"><span class="dot"></span>Schema Paladin</div></section>
<section class="slide bg-red"><div class="brand white" style="left:146px;top:20px;font-size:8px"><span class="dot"></span>Schema Paladin</div></section>

<!-- 10 quote -->
<section class="slide">
  <div class="corner">Schema Paladin</div>
  <div class="abs" style="left:170px;top:40px;font-size:56px;font-weight:700;color:#d0d0d0;line-height:1">&ldquo;</div>
  <div class="pill" style="left:58px;top:144px;width:100px;height:13px;font-size:6px;line-height:13px">Your Name</div>
  <div class="side">Schema Paladin</div>
  <div class="pg">10</div>
</section>

<!-- 11 about photo -->
<section class="slide">
  <div class="corner">Schema Paladin</div>
  <div class="abs" style="left:20px;top:40px;width:80px;height:80px;border-radius:50%;background:linear-gradient(135deg,#4a6aa2,#1e4280)" role="img" aria-label="Profile photo placeholder"></div>
  <div class="abs" style="left:45px;top:55px;width:76px;height:76px;border-radius:50%;background:#cfcfcf;box-shadow:2px 3px 6px rgba(0,0,0,.2)"></div>
  <div class="abs" style="left:143px;top:30px;width:1px;height:160px;background:#ddd"></div>
  <div class="dash" style="left:156px;top:62px"></div>
  <div class="abs" style="left:40px;top:150px;display:grid;gap:7px">
    <span style="width:5px;height:5px;border-radius:50%;background:var(--navy);display:block"></span>
    <span style="width:5px;height:5px;border-radius:50%;background:var(--navy);display:block"></span>
    <span style="width:5px;height:5px;border-radius:50%;background:var(--navy);display:block"></span>
  </div>
  <div class="side">Schema Paladin</div>
  <div class="pg">11</div>
</section>

<!-- 12 about me -->
<section class="slide">
  <div class="corner">Schema Paladin</div>
  <div class="abs" style="left:20px;top:40px;width:80px;height:80px;border-radius:50%;background:linear-gradient(135deg,#4a6aa2,#1e4280)" role="img" aria-label="Profile photo placeholder"></div>
  <div class="abs" style="left:153px;top:34px;font-size:7px;color:var(--red)">Manager</div>
  <div class="abs" style="left:153px;top:44px;font-size:14px;font-weight:600;color:var(--navy)">Name, Last Name</div>
  <div class="abs fine" style="left:153px;top:74px;width:205px">Lorem ipsum dolor sit amet, consectetur adipiscing elit, sed do eiusmod tempor incididunt ut labore et dolore magna aliqua.</div>
  <div class="abs fine" style="left:153px;top:112px;width:205px">Lorem ipsum dolor sit amet, consectetur adipiscing elit, sed do eiusmod tempor incididunt ut labore et dolore magna aliqua.</div>
  <div class="abs" style="left:38px;top:146px;display:grid;gap:6px;font-size:4.2px;color:var(--red)">
    <div style="display:flex;gap:6px;align-items:center"><span style="width:5px;height:5px;border-radius:50%;background:var(--navy)"></span>Here is a place for text</div>
    <div style="display:flex;gap:6px;align-items:center"><span style="width:5px;height:5px;border-radius:50%;background:var(--navy)"></span>Here is a place for text</div>
    <div style="display:flex;gap:6px;align-items:center"><span style="width:5px;height:5px;border-radius:50%;background:var(--navy)"></span>Here is a place for text</div>
  </div>
  <div class="side">Schema Paladin</div>
  <div class="pg">12</div>
</section>

<!-- 13 agenda -->
<section class="slide">
  <div class="corner">Schema Paladin</div>
  <div class="abs" style="left:0;top:0;width:152px;height:140px;background:var(--navy)"></div>
  <div class="abs" style="left:36px;top:28px;width:178px;height:160px;background:#fff;box-shadow:0 2px 8px rgba(0,0,0,.15)"></div>
  <ol class="abs" style="left:54px;top:46px;font-size:5px;color:var(--navy);line-height:19.5px;list-style-position:inside">
    <li>Lorem ipsum dolor sit amet</li><li>Lorem ipsum dolor sit amet</li><li>Lorem ipsum dolor sit amet</li><li>Lorem ipsum dolor sit amet</li><li>Lorem ipsum dolor sit amet</li><li>Lorem ipsum dolor sit amet</li><li>Lorem ipsum dolor sit amet</li>
  </ol>
  <div class="abs" style="left:229px;top:78px;font-size:14px;font-weight:600;color:var(--navy);line-height:1.15">Here Goes<br>Title Of Your<br>Agenda</div>
  <div class="abs" style="left:229px;top:132px;font-size:6px;color:var(--red)">Here Goes A Short Subtitle</div>
  <div class="side">Schema Paladin</div>
  <div class="pg">13</div>
</section>

<!-- 14 title and body -->
<section class="slide">
  <div class="corner">Schema Paladin</div>
  <div class="h-left" style="left:14px;top:14px">Title And Body Slide</div>
  <div class="side">Schema Paladin</div>
  <div class="pg">14</div>
</section>

<!-- 15 -->
<section class="slide">
  <div class="corner">Schema Paladin</div>
  <div class="dash" style="left:34px;top:38px"></div>
  <div class="side left">Schema Paladin</div>
  <div class="pg left">15</div>
</section>

<!-- 16 -->
<section class="slide">
  <div class="corner">Schema Paladin</div>
  <div class="h-left" style="left:18px;top:14px">Title And Body Slide</div>
  <div class="side">Schema Paladin</div>
  <div class="pg">16</div>
</section>

<!-- 17 -->
<section class="slide">
  <div class="corner">Schema Paladin</div>
  <div class="dash" style="left:30px;top:34px"></div>
  <div class="side left">Schema Paladin</div>
  <div class="pg left">17</div>
</section>

<!-- 18 navy title -->
<section class="slide bg-navy">
  <div class="corner" style="color:#fff">Schema Paladin</div>
  <div class="h-left white" style="left:18px;top:14px">Title And Body Slide</div>
  <div class="side white">Schema Paladin</div>
  <div class="pg" style="color:#c9d3e6">18</div>
</section>

<!-- 19 -->
<section class="slide bg-navy">
  <div class="corner" style="color:#fff">Schema Paladin</div>
  <div class="dash" style="left:32px;top:34px"></div>
  <div class="side left white">Schema Paladin</div>
  <div class="pg left" style="color:#c9d3e6">19</div>
</section>

<!-- 20 -->
<section class="slide">
  <div class="corner">Schema Paladin</div>
  <div class="dash" style="left:14px;top:34px"></div>
</section>

<!-- 21 -->
<section class="slide">
  <div class="corner">Schema Paladin</div>
  <div class="dash" style="left:30px;top:34px"></div>
  <div class="side left">Schema Paladin</div>
  <div class="pg left">21</div>
</section>

<!-- 22 brand break -->
<section class="slide">
  <div class="brand" style="left:104px;top:92px;font-size:20px"><span class="dot"></span>Schema Paladin</div>
  <div class="abs" style="left:0;right:0;bottom:0;height:8px;background:var(--red)"></div>
</section>

<!-- 23 slide break -->
<section class="slide bg-navy">
  <div class="abs" style="left:24px;top:40px;font-size:48px;font-weight:300;color:rgba(255,255,255,.18);line-height:1">01</div>
  <div class="abs" style="left:44px;top:54px;font-size:30px;font-weight:300;color:#fff;line-height:1">Slide<br>Break</div>
  <div class="abs fine white" style="left:44px;top:122px;width:170px">Lorem ipsum dolor sit amet, consectetur adipiscing elit, sed do eiusmod tempor incididunt ut labore et dolore magna aliqua. Lorem ipsum dolor sit amet, sed do eiusmod tempor.</div>
</section>

<!-- 24 demo circle -->
<section class="slide">
  <div class="photo-navy" role="img" aria-label="Photo of a workspace, navy tinted"></div>
  <div class="abs" style="left:103px;top:18px;width:182px;height:182px;border-radius:50%;border:1.5px solid rgba(255,255,255,.8)"></div>
  <div class="abs" style="left:0;right:0;top:48px;text-align:center;color:var(--red);font-size:15px;font-weight:600">&mdash; DEMO &mdash;</div>
  <div class="abs fine white" style="left:126px;top:76px;width:136px;text-align:center">Lorem ipsum dolor sit amet, consectetur adipiscing elit, sed do eiusmod tempor incididunt ut labore et dolore magna aliqua. Lorem ipsum dolor sit amet, consectetur adipiscing elit, sed do eiusmod tempor incididunt ut labore et dolore magna aliqua. Lorem ipsum dolor sit amet.</div>
</section>

<!-- 25 demo navy -->
<section class="slide bg-navy">
  <div class="abs" style="left:80px;top:-4px;width:226px;height:226px;border-radius:50%;background:var(--navy-deep)"></div>
  <div class="abs" style="left:102px;top:18px;width:182px;height:182px;border-radius:50%;border:1.5px solid rgba(255,255,255,.85)"></div>
  <div class="abs" style="left:0;right:0;top:46px;text-align:center;color:#fff;font-size:15px;font-weight:600">&mdash; DEMO &mdash;</div>
  <div class="abs fine white" style="left:124px;top:74px;width:140px;text-align:center">Lorem ipsum dolor sit amet, consectetur adipiscing elit, sed do eiusmod tempor incididunt ut labore et dolore magna aliqua. Lorem ipsum dolor sit amet, consectetur adipiscing elit, sed do eiusmod tempor incididunt ut labore et dolore magna aliqua. Lorem ipsum dolor sit amet.</div>
</section>

<!-- 26 demo split -->
<section class="slide">
  <div class="photo-navy" role="img" aria-label="Photo of a laptop, navy tinted"></div>
  <div class="brand white" style="left:26px;top:100px;font-size:9px"><span class="dot"></span>Schema Paladin</div>
  <div class="abs" style="left:150px;top:70px;width:1.5px;height:86px;background:var(--red)"></div>
  <div class="pill" style="left:164px;top:68px;width:80px;height:17px;font-size:10px;line-height:17px">DEMO</div>
  <div class="abs" style="left:166px;top:92px;width:196px;font-size:6.5px;line-height:1.35;color:#e6ebf4">Lorem ipsum dolor sit amet, consectetur adipiscing elit, sed do eiusmod tempor incididunt ut labore et dolore magna aliqua. Lorem ipsum dolor sit amet, consectetur adipiscing elit, sed do eiusmod tempor incididunt ut labore et dolore magna aliqua.</div>
</section>

<!-- 27 pic and text -->
<section class="slide">
  <div class="corner">Schema Paladin</div>
  <div class="h-left" style="left:20px;top:58px;font-size:17px">Pic And Text</div>
  <div class="abs fine" style="left:20px;top:94px;width:130px;text-align:justify">Lorem ipsum dolor sit amet, consectetur adipiscing elit, sed do eiusmod tempor incididunt ut labore et dolore magna aliqua. Lorem ipsum dolor sit amet, consectetur adipiscing elit, sed do eiusmod tempor incididunt ut labore et dolore magna aliqua. Ut enim ad minim veniam, quis nostrud exercitation ullamco laboris nisi ut aliquip.</div>
  <div class="abs" style="left:206px;top:22px;width:106px;height:72px;background:var(--red)"></div>
  <div class="photo-light" style="left:190px;top:36px;width:166px;height:142px;box-shadow:0 3px 8px rgba(0,0,0,.2)" role="img" aria-label="Photo of hands using a computer at a desk"></div>
  <div class="side">Schema Paladin</div>
  <div class="pg">27</div>
</section>

<!-- 28 -->
<section class="slide">
  <div class="corner">Schema Paladin</div>
  <div class="abs" style="left:190px;top:61px;width:44px;height:2px;background:var(--red)"></div>
  <div class="abs" style="left:87px;top:144px;width:287px;height:73px;background:var(--navy);border-radius:22px 0 0 0"></div>
  <div class="side">Schema Paladin</div>
</section>

<!-- 29 awesome text -->
<section class="slide">
  <div class="abs" style="left:0;top:0;right:14px;height:106px;background:var(--navy)"></div>
  <div class="abs" style="left:0;right:14px;top:32px;text-align:center;color:#fff;font-size:15px;font-weight:600">Here Add Awesome Text</div>
  <div class="abs" style="left:54px;top:91px;width:30px;height:30px;border-radius:50%;background:var(--red);border:2px solid #fff"></div>
  <div class="abs" style="left:160px;top:91px;width:30px;height:30px;border-radius:50%;background:var(--red);border:2px solid #fff"></div>
  <div class="abs" style="left:266px;top:91px;width:30px;height:30px;border-radius:50%;background:var(--red);border:2px solid #fff"></div>
  <div class="abs" style="left:28px;top:136px;width:82px;text-align:center"><div class="label">Project name</div><div class="fine" style="margin-top:3px">Lorem ipsum dolor sit amet, nec an dictas equidem appellantur, ut has commune.</div></div>
  <div class="abs" style="left:134px;top:136px;width:82px;text-align:center"><div class="label">Project name</div><div class="fine" style="margin-top:3px">Lorem ipsum dolor sit amet, nec an dictas equidem appellantur, ut has commune.</div></div>
  <div class="abs" style="left:240px;top:136px;width:82px;text-align:center"><div class="label">Project name</div><div class="fine" style="margin-top:3px">Lorem ipsum dolor sit amet, nec an dictas equidem appellantur, ut has commune.</div></div>
  <div class="side">Schema Paladin</div>
  <div class="pg left">29</div>
</section>

<!-- 30 three columns -->
<section class="slide">
  <div class="corner">Schema Paladin</div>
  <div class="h-title">3 Columns Slide</div>
  <div class="card c-red" style="left:43px;top:86px;width:88px;height:80px"><span class="ic"></span><div class="nm">Project name here</div><div class="tx">Lorem ipsum dolor sit amet, nec an dictas equidem appellantur, ut has commune.</div></div>
  <div class="card c-navy" style="left:142px;top:86px;width:88px;height:80px"><span class="ic"></span><div class="nm">Project name here</div><div class="tx">Lorem ipsum dolor sit amet, nec an dictas equidem appellantur, ut has commune.</div></div>
  <div class="card c-gray" style="left:241px;top:86px;width:88px;height:80px"><span class="ic"></span><div class="nm">Project name here</div><div class="tx">Lorem ipsum dolor sit amet, nec an dictas equidem appellantur, ut has commune.</div></div>
  <div class="side">Schema Paladin</div>
  <div class="pg">30</div>
</section>

<!-- 31 four columns -->
<section class="slide">
  <div class="corner">Schema Paladin</div>
  <div class="h-title">4 Column Slide</div>
  <div class="card c-red" style="left:22px;top:82px;width:81px;height:102px"><span class="ic"></span><div class="nm">Project name here</div><div class="tx">Lorem ipsum dolor sit amet, nec an dictas equidem appellantur, ut has commune accommodare.</div></div>
  <div class="card c-navy" style="left:109px;top:82px;width:81px;height:102px"><span class="ic"></span><div class="nm">Project name here</div><div class="tx">Lorem ipsum dolor sit amet, nec an dictas equidem appellantur, ut has commune accommodare.</div></div>
  <div class="card c-deep" style="left:196px;top:82px;width:81px;height:102px"><span class="ic"></span><div class="nm">Project name here</div><div class="tx">Lorem ipsum dolor sit amet, nec an dictas equidem appellantur, ut has commune accommodare.</div></div>
  <div class="card c-gray" style="left:283px;top:82px;width:81px;height:102px"><span class="ic"></span><div class="nm">Project name here</div><div class="tx">Lorem ipsum dolor sit amet, nec an dictas equidem appellantur, ut has commune accommodare.</div></div>
  <div class="side">Schema Paladin</div>
  <div class="pg">31</div>
</section>

<!-- 32 five columns -->
<section class="slide">
  <div class="corner">Schema Paladin</div>
  <div class="h-title">5 Column Slide</div>
  <div class="card c-navy" style="left:44px;top:65px;width:88px;height:54px;padding-top:7px"><div class="nm">Project name here</div><div class="tx">Lorem ipsum dolor sit amet, nec an dictas equidem appellantur, ut has commune.</div></div>
  <div class="card c-navy" style="left:142px;top:65px;width:88px;height:54px;padding-top:7px"><div class="nm">Project name here</div><div class="tx">Lorem ipsum dolor sit amet, nec an dictas equidem appellantur, ut has commune.</div></div>
  <div class="card c-navy" style="left:239px;top:65px;width:88px;height:54px;padding-top:7px"><div class="nm">Project name here</div><div class="tx">Lorem ipsum dolor sit amet, nec an dictas equidem appellantur, ut has commune.</div></div>
  <div class="card c-navy" style="left:89px;top:128px;width:88px;height:56px;padding-top:7px"><div class="nm">Project name here</div><div class="tx">Lorem ipsum dolor sit amet, nec an dictas equidem appellantur, ut has commune.</div></div>
  <div class="card c-navy" style="left:187px;top:128px;width:90px;height:56px;padding-top:7px"><div class="nm">Project name here</div><div class="tx">Lorem ipsum dolor sit amet, nec an dictas equidem appellantur, ut has commune.</div></div>
  <div class="side">Schema Paladin</div>
  <div class="pg">32</div>
</section>

<!-- 33 screenshot -->
<section class="slide">
  <svg class="abs" style="left:0;top:0" width="386" height="217"><polygon points="0,0 386,0 386,100 250,217 0,217" fill="var(--navy)"/></svg>
  <div class="corner" style="color:#fff">Schema Paladin</div>
  <div class="h-left white" style="left:20px;top:68px;font-size:14px;line-height:1.2">A Place for<br>Screenshot</div>
  <div class="abs fine white" style="left:20px;top:124px;width:120px">Lorem ipsum dolor sit amet, consectetur adipiscing elit, sed do eiusmod tempor ut labore et dolore.</div>
  <div class="abs" style="left:162px;top:50px;width:196px;height:124px;background:#1d1d1d;border-radius:5px 5px 0 0;padding:6px"><div style="width:100%;height:100%;background:#7c7c7c;color:#fff;font-size:6px;font-weight:600;display:flex;align-items:center;justify-content:center">HERE YOU CAN ADD A SCREENSHOT</div></div>
  <div class="abs" style="left:150px;top:174px;width:220px;height:6px;background:#c7c7c9;border-radius:0 0 6px 6px"></div>
  <div class="side">Schema Paladin</div>
  <div class="pg">33</div>
</section>

<!-- 34 six columns -->
<section class="slide">
  <div class="corner">Schema Paladin</div>
  <div class="h-title">6 Columns Slide</div>
  <div class="abs" style="left:30px;top:66px;display:grid;grid-template-columns:150px 150px;row-gap:16px;column-gap:22px">
    <div style="display:flex;gap:10px"><span style="width:12px;height:12px;border:1px solid var(--navy);flex:none"></span><div><div class="label">Project name</div><div class="fine">Lorem ipsum dolor sit amet, nec an dictas equidem appellantur, ut has commune.</div></div></div>
    <div style="display:flex;gap:10px"><span style="width:12px;height:12px;border:1px solid var(--navy);flex:none"></span><div><div class="label">Project name</div><div class="fine">Lorem ipsum dolor sit amet, nec an dictas equidem appellantur, ut has commune.</div></div></div>
    <div style="display:flex;gap:10px"><span style="width:12px;height:12px;border:1px solid var(--navy);flex:none"></span><div><div class="label">Project name</div><div class="fine">Lorem ipsum dolor sit amet, nec an dictas equidem appellantur, ut has commune.</div></div></div>
    <div style="display:flex;gap:10px"><span style="width:12px;height:12px;border:1px solid var(--navy);flex:none"></span><div><div class="label">Project name</div><div class="fine">Lorem ipsum dolor sit amet, nec an dictas equidem appellantur, ut has commune.</div></div></div>
    <div style="display:flex;gap:10px"><span style="width:12px;height:12px;border:1px solid var(--navy);flex:none"></span><div><div class="label">Project name</div><div class="fine">Lorem ipsum dolor sit amet, nec an dictas equidem appellantur, ut has commune.</div></div></div>
    <div style="display:flex;gap:10px"><span style="width:12px;height:12px;border:1px solid var(--navy);flex:none"></span><div><div class="label">Project name</div><div class="fine">Lorem ipsum dolor sit amet, nec an dictas equidem appellantur, ut has commune.</div></div></div>
  </div>
  <div class="side">Schema Paladin</div>
  <div class="pg">34</div>
</section>

<!-- 35 table ticks -->
<section class="slide">
  <div class="corner">Schema Paladin</div>
  <div class="h-title" style="top:12px">Table Slide</div>
  <table class="tbl abs" style="left:15px;top:58px;width:338px">
    <tr><th style="background:none;width:100px"></th><th style="background:var(--red)">Your Text Here</th><th style="background:var(--red)">Your Text Here</th><th style="background:var(--red)">Your Text Here</th><th style="background:var(--red)">Your Text Here</th></tr>
    <tr><td style="background:var(--navy);color:#fff">You can replace this text</td><td>1700</td><td style="color:var(--navy);font-size:7px">&#10003;</td><td>50%</td><td>1700</td></tr>
    <tr style="background:var(--light)"><td style="background:var(--navy);color:#fff">You can replace this text</td><td>1602</td><td style="color:var(--navy);font-size:7px">&#10005;</td><td>50%</td><td>1602</td></tr>
    <tr><td style="background:var(--navy);color:#fff">You can replace this text</td><td>1500</td><td style="color:var(--navy);font-size:7px">&#10003;</td><td>12%</td><td>1500</td></tr>
    <tr style="background:var(--light)"><td style="background:var(--navy);color:#fff">You can replace this text</td><td>1315</td><td style="color:var(--navy);font-size:7px">&#10005;</td><td>45%</td><td>1315</td></tr>
    <tr><td style="background:var(--navy);color:#fff">You can replace this text</td><td>1200</td><td style="color:var(--navy);font-size:7px">&#10003;</td><td>30%</td><td>1200</td></tr>
    <tr style="background:var(--light)"><td style="background:var(--navy);color:#fff">You can replace this text</td><td>1100</td><td style="color:var(--navy);font-size:7px">&#10003;</td><td>30%</td><td>1100</td></tr>
    <tr><td style="background:var(--navy);color:#fff">You can replace this text</td><td>1050</td><td style="color:var(--navy);font-size:7px">&#10005;</td><td>20%</td><td>1050</td></tr>
  </table>
  <div class="side">Schema Paladin</div>
  <div class="pg">35</div>
</section>

<!-- 36 table navy -->
<section class="slide">
  <div class="abs" style="left:0;top:0;width:208px;height:217px;background:var(--navy)"></div>
  <div class="h-left white" style="left:18px;top:98px">Table Slide</div>
  <div class="abs" style="left:135px;top:35px;width:214px;height:164px;background:#fff;box-shadow:0 2px 8px rgba(0,0,0,.2);padding:10px 8px">
    <table class="tbl">
      <tr><th style="background:var(--navy)">Text</th><th style="background:var(--navy)">Text</th><th style="background:var(--navy)">Text</th><th style="background:var(--navy)">Text</th><th style="background:var(--navy)">Text</th></tr>
      <tr><td>Data</td><td>Data</td><td>Data</td><td>Data</td><td>Data</td></tr>
      <tr style="background:var(--light)"><td>Data</td><td>Data</td><td>Data</td><td>Data</td><td>Data</td></tr>
      <tr><td>Data</td><td>Data</td><td>Data</td><td>Data</td><td>Data</td></tr>
      <tr style="background:var(--light)"><td>Data</td><td>Data</td><td>Data</td><td>Data</td><td>Data</td></tr>
      <tr><td>Data</td><td>Data</td><td>Data</td><td>Data</td><td>Data</td></tr>
      <tr style="background:var(--light)"><td>Data</td><td>Data</td><td>Data</td><td>Data</td><td>Data</td></tr>
      <tr><td>Data</td><td>Data</td><td>Data</td><td>Data</td><td>Data</td></tr>
    </table>
  </div>
  <div class="side">Schema Paladin</div>
  <div class="pg">36</div>
</section>

<!-- 37 table simple -->
<section class="slide">
  <div class="corner">Schema Paladin</div>
  <div class="h-title">Table Slide</div>
  <table class="tbl abs" style="left:42px;top:62px;width:318px">
    <tr><th style="background:var(--navy)">Text</th><th style="background:var(--navy)">Text</th><th style="background:var(--navy)">Text</th><th style="background:var(--navy)">Text</th><th style="background:var(--navy)">Text</th></tr>
    <tr><td>Data</td><td>Data</td><td>Data</td><td>Data</td><td>Data</td></tr>
    <tr style="background:var(--light)"><td>Data</td><td>Data</td><td>Data</td><td>Data</td><td>Data</td></tr>
    <tr><td>Data</td><td>Data</td><td>Data</td><td>Data</td><td>Data</td></tr>
    <tr style="background:var(--light)"><td>Data</td><td>Data</td><td>Data</td><td>Data</td><td>Data</td></tr>
    <tr><td>Data</td><td>Data</td><td>Data</td><td>Data</td><td>Data</td></tr>
    <tr style="background:var(--light)"><td>Data</td><td>Data</td><td>Data</td><td>Data</td><td>Data</td></tr>
    <tr><td>Data</td><td>Data</td><td>Data</td><td>Data</td><td>Data</td></tr>
  </table>
  <div class="abs" style="left:42px;top:188px;width:318px;height:1px;background:#ccc"></div>
  <div class="side">Schema Paladin</div>
  <div class="pg">37</div>
</section>

<!-- 38 smart art -->
<section class="slide">
  <div class="corner">Schema Paladin</div>
  <div class="h-left" style="left:20px;top:14px">Smart Art Slide</div>
  <div class="abs" style="left:20px;top:58px;display:grid;row-gap:20px;width:150px">
    <div style="display:flex;gap:8px"><span style="width:10px;height:10px;border-radius:50%;border:1px solid var(--navy);flex:none"></span><div><div class="label">Lorem ipsum dolor</div><div class="fine">Lorem ipsum dolor sit amet, consectetur adipiscing elit, sed do eiusmod tempor.</div></div></div>
    <div style="display:flex;gap:8px"><span style="width:10px;height:10px;border-radius:50%;border:1px solid var(--navy);flex:none"></span><div><div class="label">Lorem ipsum dolor</div><div class="fine">Lorem ipsum dolor sit amet, consectetur adipiscing elit, sed do eiusmod tempor.</div></div></div>
    <div style="display:flex;gap:8px"><span style="width:10px;height:10px;border-radius:50%;border:1px solid var(--navy);flex:none"></span><div><div class="label">Lorem ipsum dolor</div><div class="fine">Lorem ipsum dolor sit amet, consectetur adipiscing elit, sed do eiusmod tempor.</div></div></div>
  </div>
  <svg class="abs" style="left:0;top:0" width="386" height="217">
    <g stroke="#fff" stroke-width="3" stroke-linejoin="round">
      <polygon points="272,31 231.5,108.5 312.5,108.5" fill="var(--navy)"/>
      <polygon points="231.5,108.5 191,186 272,186" fill="var(--red)"/>
      <polygon points="231.5,108.5 312.5,108.5 272,186" fill="var(--navy)"/>
      <polygon points="312.5,108.5 272,186 353,186" fill="#8a8a8a"/>
    </g>
    <g fill="#fff" font-family="Poppins,sans-serif" font-size="4.5" font-weight="600" text-anchor="middle">
      <text x="272" y="84">Project</text><text x="272" y="90">name</text>
      <text x="272" y="126">Project name</text>
      <text x="229" y="162">Project name</text>
      <text x="315" y="162">Project name</text>
    </g>
  </svg>
  <div class="side">Schema Paladin</div>
  <div class="pg">38</div>
</section>

<!-- 39 quotes -->
<section class="slide">
  <div class="corner">Schema Paladin</div>
  <div class="h-title" style="top:12px">Here is Quotes</div>
  <div class="abs" style="left:26px;top:56px;width:150px">
    <div style="color:var(--red);font-size:22px;font-weight:700;line-height:1">&rdquo;</div>
    <div class="fine" style="margin-top:2px">Lorem ipsum dolor sit amet, consectetur adipiscing elit, sed do eiusmod tempor incididunt ut labore et dolore magna aliqua. Lorem ipsum dolor sit amet, consectetur adipiscing elit.</div>
    <div style="display:flex;gap:8px;align-items:center;margin-top:22px"><span style="width:18px;height:18px;border-radius:50%;background:#d9d9d9"></span><div class="fine"><b style="color:var(--ink)">Your Name</b><br>Founder</div></div>
  </div>
  <div class="abs" style="left:202px;top:56px;width:150px">
    <div style="color:var(--navy);font-size:22px;font-weight:700;line-height:1">&rdquo;</div>
    <div class="fine" style="margin-top:2px">Lorem ipsum dolor sit amet, consectetur adipiscing elit, sed do eiusmod tempor incididunt ut labore et dolore magna aliqua. Lorem ipsum dolor sit amet, consectetur adipiscing elit.</div>
    <div style="display:flex;gap:8px;align-items:center;margin-top:22px"><span style="width:18px;height:18px;border-radius:50%;background:#d9d9d9"></span><div class="fine"><b style="color:var(--ink)">Your Name</b><br>Founder</div></div>
  </div>
  <div class="side">Schema Paladin</div>
  <div class="pg">39</div>
</section>

<!-- 40 statistics circles -->
<section class="slide">
  <div class="corner">Schema Paladin</div>
  <div class="h-title">Here Is Statistics</div>
  <svg class="abs" style="left:0;top:0" width="386" height="217">
    <circle cx="82" cy="128" r="58" fill="var(--navy)"/>
    <circle cx="82" cy="142" r="40" fill="var(--red)"/>
    <circle cx="82" cy="158" r="22" fill="#1b3560"/>
    <g stroke="#999" stroke-width=".6"><line x1="104" y1="94" x2="158" y2="94"/><line x1="120" y1="128" x2="158" y2="128"/><line x1="104" y1="160" x2="158" y2="160"/></g>
    <g fill="#fff" font-family="Poppins,sans-serif" font-size="11" font-weight="600" text-anchor="middle"><text x="82" y="98">$</text><text x="82" y="132">$</text><text x="82" y="166">$</text></g>
    <g fill="var(--navy)" font-family="Poppins,sans-serif" font-size="9" font-weight="600"><text x="166" y="97">5M</text><text x="166" y="131">2M</text><text x="166" y="163">1M</text></g>
  </svg>
  <div class="abs" style="left:226px;top:84px;display:grid;row-gap:13px;width:130px">
    <div style="display:flex;gap:6px"><span style="width:11px;height:11px;background:var(--navy);color:#fff;font-size:8px;line-height:11px;text-align:center;flex:none">&#10003;</span><div><div class="label">Lorem ipsum dolor</div><div class="fine">Lorem ipsum dolor sit amet, consectetur adipiscing elit.</div></div></div>
    <div style="display:flex;gap:6px"><span style="width:11px;height:11px;background:var(--red);color:#fff;font-size:8px;line-height:11px;text-align:center;flex:none">&#10003;</span><div><div class="label">Lorem ipsum dolor</div><div class="fine">Lorem ipsum dolor sit amet, consectetur adipiscing elit.</div></div></div>
    <div style="display:flex;gap:6px"><span style="width:11px;height:11px;background:#555;color:#fff;font-size:8px;line-height:11px;text-align:center;flex:none">&#10003;</span><div><div class="label">Lorem ipsum dolor</div><div class="fine">Lorem ipsum dolor sit amet, consectetur adipiscing elit.</div></div></div>
  </div>
  <div class="side">Schema Paladin</div>
  <div class="pg">40</div>
</section>

<!-- 41 ring percentages -->
<section class="slide">
  <div class="corner">Schema Paladin</div>
  <div class="h-title" style="top:12px">Here Add Your Title</div>
  <div class="abs fine" style="left:62px;top:52px;width:262px;text-align:center">Lorem Ipsum is simply dummy text of the printing and typesetting industry. Lorem Ipsum has been the industry's standard dummy text ever since the 1500s, when an unknown printer took a galley of type and scrambled it.</div>
  <svg class="abs" style="left:0;top:0" width="386" height="217">
    <g fill="none" stroke-width="5">
      <circle cx="96" cy="129" r="24" stroke="#e6e6e6"/><circle cx="96" cy="129" r="24" stroke="var(--red)" stroke-dasharray="75.4 150.8" transform="rotate(-90 96 129)"/>
      <circle cx="177" cy="129" r="24" stroke="#e6e6e6"/><circle cx="177" cy="129" r="24" stroke="var(--red)" stroke-dasharray="113.1 150.8" transform="rotate(-90 177 129)"/>
      <circle cx="259" cy="129" r="24" stroke="#e6e6e6"/><circle cx="259" cy="129" r="24" stroke="var(--red)" stroke-dasharray="60.3 150.8" transform="rotate(-90 259 129)"/>
    </g>
    <g fill="var(--navy)" font-family="Poppins,sans-serif" font-size="12" font-weight="600" text-anchor="middle"><text x="96" y="133">50%</text><text x="177" y="133">75%</text><text x="259" y="133">40%</text></g>
  </svg>
  <div class="abs fine" style="left:70px;top:162px;width:52px;text-align:center">Lorem ipsum dolor amet consectetur</div>
  <div class="abs fine" style="left:151px;top:162px;width:52px;text-align:center">Lorem ipsum dolor amet consectetur</div>
  <div class="abs fine" style="left:233px;top:162px;width:52px;text-align:center">Lorem ipsum dolor amet consectetur</div>
  <div class="side">Schema Paladin</div>
  <div class="pg">41</div>
</section>

<!-- 42 revenue chart -->
<section class="slide">
  <div class="corner">Schema Paladin</div>
  <div class="h-title" style="top:12px">Here is Statistics</div>
  <div class="abs" style="left:15px;top:66px;width:92px;height:56px;background:var(--navy);color:#fff;text-align:center;padding-top:12px"><div style="font-size:13px">$0.5M</div><div style="font-size:4.5px;opacity:.85">Revenue</div></div>
  <div class="abs" style="left:15px;top:127px;width:92px;height:58px;background:#fff;box-shadow:0 1px 5px rgba(0,0,0,.15);color:var(--red);text-align:center;padding-top:14px"><div style="font-size:13px">-0.28%</div><div style="font-size:4.5px">Revenue</div></div>
  <svg class="abs" style="left:0;top:0" width="386" height="217">
    <g stroke="#eee" stroke-width=".6"><line x1="170" y1="72" x2="355" y2="72"/><line x1="170" y1="90" x2="355" y2="90"/><line x1="170" y1="108" x2="355" y2="108"/><line x1="170" y1="126" x2="355" y2="126"/><line x1="170" y1="144" x2="355" y2="144"/><line x1="170" y1="162" x2="355" y2="162"/></g>
    <g fill="#999" font-family="Poppins,sans-serif" font-size="3.6"><text x="148" y="73">$600,000</text><text x="148" y="91">$500,000</text><text x="148" y="109">$400,000</text><text x="148" y="127">$300,000</text><text x="148" y="145">$200,000</text><text x="148" y="163">$100,000</text><text x="148" y="180">$0</text></g>
    <polyline fill="none" stroke="var(--red)" stroke-width="1.2" points="172,170 186,162 198,150 210,156 222,140 236,148 248,152 262,146 276,160 290,150 304,130 318,138 332,118 346,96 354,84"/>
    <g fill="#999" font-family="Poppins,sans-serif" font-size="3.6"><text x="170" y="188">Jan</text><text x="186" y="188">Feb</text><text x="201" y="188">Mar</text><text x="216" y="188">Apr</text><text x="231" y="188">May</text><text x="246" y="188">Jun</text><text x="261" y="188">Jul</text><text x="276" y="188">Aug</text><text x="291" y="188">Sep</text><text x="306" y="188">Oct</text><text x="321" y="188">Nov</text><text x="337" y="188">Dec</text></g>
  </svg>
  <div class="side">Schema Paladin</div>
  <div class="pg">42</div>
</section>

<!-- 43 timeline -->
<section class="slide">
  <div class="corner">Schema Paladin</div>
  <div class="h-title" style="top:12px">Company Timeline</div>
  <svg class="abs" style="left:0;top:0" width="386" height="217">
    <g fill="var(--red)">
      <polygon points="42,79 100,79 108,91 100,103 42,103 50,91"/>
      <polygon points="104,79 162,79 170,91 162,103 104,103 112,91"/>
      <polygon points="166,79 224,79 232,91 224,103 166,103 174,91"/>
      <polygon points="228,79 286,79 294,91 286,103 228,103 236,91"/>
      <polygon points="290,79 348,79 356,91 348,103 290,103 298,91"/>
    </g>
    <g fill="#fff" font-family="Poppins,sans-serif" font-size="6" font-weight="600" text-anchor="middle"><text x="78" y="93">STEP 01</text><text x="140" y="93">STEP 02</text><text x="202" y="93">STEP 03</text><text x="264" y="93">STEP 04</text><text x="326" y="93">STEP 05</text></g>
    <line x1="42" y1="110" x2="358" y2="110" stroke="#bbb" stroke-width=".8"/>
    <g stroke="#bbb" stroke-width=".8"><line x1="68" y1="110" x2="68" y2="140"/><line x1="131" y1="110" x2="131" y2="140"/><line x1="194" y1="110" x2="194" y2="140"/><line x1="258" y1="110" x2="258" y2="140"/><line x1="321" y1="110" x2="321" y2="140"/></g>
  </svg>
  <div class="abs" style="left:42px;top:144px;display:grid;grid-template-columns:repeat(5,58px);column-gap:5px;text-align:center">
    <div><div class="label">Project name</div><div class="fine">Lorem Ipsum is simply dummy text of type.</div></div>
    <div><div class="label">Project name</div><div class="fine">Lorem Ipsum is simply dummy text of type.</div></div>
    <div><div class="label">Project name</div><div class="fine">Lorem Ipsum is simply dummy text of type.</div></div>
    <div><div class="label">Project name</div><div class="fine">Lorem Ipsum is simply dummy text of type.</div></div>
    <div><div class="label">Project name</div><div class="fine">Lorem Ipsum is simply dummy text of type.</div></div>
  </div>
  <div class="side">Schema Paladin</div>
  <div class="pg">43</div>
</section>

<!-- 44 Q&A -->
<section class="slide">
  <div class="corner">Schema Paladin</div>
  <div class="h-title" style="top:12px">Q&amp;A Slide</div>
  <div class="abs" style="left:44px;top:66px;display:grid;grid-template-columns:160px 140px;row-gap:13px;column-gap:15px">
    <div style="display:flex;gap:10px"><span style="width:18px;height:18px;background:var(--navy);color:#fff;font-size:8px;font-weight:600;text-align:center;line-height:18px;flex:none">Q</span><div class="fine">Lorem Ipsum is simply dummy unknown printer took a galley of type and scrambled it to make.</div></div>
    <div style="display:flex;gap:10px"><span style="width:18px;height:18px;background:var(--red);color:#fff;font-size:8px;font-weight:600;text-align:center;line-height:18px;flex:none">A</span><div class="fine">type and scrambled it to make. Lorem Ipsum is simply dummy unknown printer took a galley of.</div></div>
    <div style="display:flex;gap:10px"><span style="width:18px;height:18px;background:var(--navy);color:#fff;font-size:8px;font-weight:600;text-align:center;line-height:18px;flex:none">Q</span><div class="fine">Lorem Ipsum is simply dummy unknown printer took a galley of type and scrambled it to make.</div></div>
    <div style="display:flex;gap:10px"><span style="width:18px;height:18px;background:var(--red);color:#fff;font-size:8px;font-weight:600;text-align:center;line-height:18px;flex:none">A</span><div class="fine">type and scrambled it to make. Lorem Ipsum is simply dummy unknown printer took a galley of.</div></div>
    <div style="display:flex;gap:10px"><span style="width:18px;height:18px;background:var(--navy);color:#fff;font-size:8px;font-weight:600;text-align:center;line-height:18px;flex:none">Q</span><div class="fine">Lorem Ipsum is simply dummy unknown printer took a galley of type and scrambled it to make.</div></div>
    <div style="display:flex;gap:10px"><span style="width:18px;height:18px;background:var(--red);color:#fff;font-size:8px;font-weight:600;text-align:center;line-height:18px;flex:none">A</span><div class="fine">type and scrambled it to make. Lorem Ipsum is simply dummy unknown printer took a galley of.</div></div>
    <div style="display:flex;gap:10px"><span style="width:18px;height:18px;background:var(--navy);color:#fff;font-size:8px;font-weight:600;text-align:center;line-height:18px;flex:none">Q</span><div class="fine">Lorem Ipsum is simply dummy unknown printer took a galley of type and scrambled it to make.</div></div>
    <div style="display:flex;gap:10px"><span style="width:18px;height:18px;background:var(--red);color:#fff;font-size:8px;font-weight:600;text-align:center;line-height:18px;flex:none">A</span><div class="fine">type and scrambled it to make. Lorem Ipsum is simply dummy unknown printer took a galley of.</div></div>
  </div>
  <div class="side">Schema Paladin</div>
  <div class="pg">44</div>
</section>

<!-- 45 thank you -->
<section class="slide">
  <div class="brand" style="left:50px;top:56px;font-size:8px"><span class="dot"></span>Schema Paladin</div>
  <div class="abs" style="left:44px;top:82px;width:105px;height:84px;box-shadow:0 1px 5px rgba(0,0,0,.15);background:#fff">
    <div style="height:28px;background:var(--navy);display:flex;align-items:center;gap:8px;padding-left:10px;font-size:4px;color:#fff"><span style="width:6px;height:6px;border-radius:50%;background:#fff"></span>www.schemapaladinhq.com</div>
    <div style="height:28px;display:flex;align-items:center;gap:8px;padding-left:10px;font-size:4px;color:#777"><span style="width:6px;height:6px;border-radius:50%;background:var(--navy)"></span>Social handle here</div>
    <div style="height:28px;display:flex;align-items:center;gap:8px;padding-left:10px;font-size:4px;color:#777"><span style="width:6px;height:6px;border:1px solid var(--navy)"></span>hello@schemapaladinhq.com</div>
  </div>
  <div class="abs" style="left:198px;top:110px;font-size:21px;font-weight:600;color:var(--navy)">THANK YOU</div>
</section>

<!-- 46 questions -->
<section class="slide">
  <svg class="abs" style="left:0;top:0" width="386" height="217">
    <polygon points="94,48 306,38 300,160 206,166 180,188 170,166 96,164" fill="none" stroke="var(--red)" stroke-width="1.5"/>
    <polygon points="88,56 314,46 310,170 208,174 184,196 172,172 92,170" fill="none" stroke="var(--navy)" stroke-width="1.5"/>
    <polygon points="102,60 296,52 292,156 112,160" fill="#fff" style="filter:drop-shadow(0 2px 4px rgba(0,0,0,.15))"/>
  </svg>
  <div class="abs" style="left:0;right:0;top:90px;text-align:center;font-size:22px;font-weight:600;color:var(--navy)">Questions?</div>
</section>

<!-- 47 icon set -->
<section class="slide">
  <div class="corner">Schema Paladin</div>
  <svg class="abs" style="left:0;top:0" width="386" height="217" aria-label="Icon set">
    <defs>
      <g id="i-db" fill="none" stroke="#333" stroke-width=".8"><ellipse cx="7" cy="3" rx="5" ry="2"/><path d="M2 3v8c0 1.1 2.2 2 5 2s5-.9 5-2V3M2 7c0 1.1 2.2 2 5 2s5-.9 5-2"/></g>
      <g id="i-gear" fill="none" stroke="#333" stroke-width=".8"><circle cx="7" cy="7" r="5"/><circle cx="7" cy="7" r="2"/></g>
      <g id="i-doc" fill="none" stroke="#333" stroke-width=".8"><rect x="3" y="1" width="9" height="12"/><path d="M5 5h5M5 8h5M5 11h3"/></g>
      <g id="i-chart" fill="none" stroke="#333" stroke-width=".8"><path d="M1 13h12"/><rect x="2" y="8" width="2" height="5"/><rect x="6" y="5" width="2" height="8"/><rect x="10" y="2" width="2" height="11"/></g>
      <g id="i-screen" fill="none" stroke="#333" stroke-width=".8"><rect x="1" y="2" width="12" height="8"/><path d="M5 13h4M7 10v3"/></g>
      <g id="i-pin" fill="none" stroke="#333" stroke-width=".8"><path d="M7 13C3 8 3 6 3 5a4 4 0 0 1 8 0c0 1 0 3-4 8z"/><circle cx="7" cy="5" r="1.4"/></g>
    </defs>
    <g transform="translate(22,37)">
      <g><use href="#i-db"/><use href="#i-gear" x="34"/><use href="#i-doc" x="68"/><use href="#i-chart" x="102"/><use href="#i-screen" x="136"/><use href="#i-pin" x="170"/><use href="#i-db" x="204"/><use href="#i-doc" x="238"/><use href="#i-screen" x="272"/><use href="#i-gear" x="306"/></g>
      <g transform="translate(0,23)"><use href="#i-screen"/><use href="#i-doc" x="34"/><use href="#i-gear" x="68"/><use href="#i-db" x="102"/><use href="#i-pin" x="136"/><use href="#i-chart" x="170"/><use href="#i-screen" x="204"/><use href="#i-gear" x="238"/><use href="#i-db" x="272"/><use href="#i-chart" x="306"/></g>
      <g transform="translate(0,46)"><use href="#i-gear"/><use href="#i-chart" x="34"/><use href="#i-pin" x="68"/><use href="#i-screen" x="102"/><use href="#i-db" x="136"/><use href="#i-doc" x="170"/><use href="#i-gear" x="204"/><use href="#i-chart" x="238"/><use href="#i-pin" x="272"/><use href="#i-doc" x="306"/></g>
      <g transform="translate(0,69)"><use href="#i-chart"/><use href="#i-db" x="34"/><use href="#i-screen" x="68"/><use href="#i-doc" x="102"/><use href="#i-gear" x="136"/><use href="#i-pin" x="170"/><use href="#i-doc" x="204"/><use href="#i-db" x="238"/><use href="#i-gear" x="272"/><use href="#i-screen" x="306"/></g>
      <g transform="translate(0,92)"><use href="#i-pin"/><use href="#i-screen" x="34"/><use href="#i-db" x="68"/><use href="#i-gear" x="102"/><use href="#i-chart" x="136"/><use href="#i-db" x="170"/><use href="#i-pin" x="204"/><use href="#i-screen" x="238"/><use href="#i-chart" x="272"/><use href="#i-db" x="306"/></g>
      <g transform="translate(0,115)"><use href="#i-doc"/><use href="#i-pin" x="34"/><use href="#i-chart" x="68"/><use href="#i-gear" x="102"/><use href="#i-doc" x="136"/><use href="#i-screen" x="170"/><use href="#i-chart" x="204"/><use href="#i-pin" x="238"/><use href="#i-doc" x="272"/><use href="#i-gear" x="306"/></g>
    </g>
  </svg>
  <div class="side">Schema Paladin</div>
</section>

</main>
</body>
</html>
```